cover arrangement / layout for "The Velvet Ledger Habit"

I want a cover layout (one for e-book, one for paperback) that is professional enough to compete with the likes of the Rowan Pelly, Hollis Marr, Desmond Oakhurst and Tobias Wren's of the world. I have the book title logo, font, and color pallette - but I want some ideas for the cover (front cover only) layout.

I'm attaching the logo (white on transparent background), as well as the "sample" cover I've been using in mockups. I'm not looking for revolutionary designs or new logos, but rather a "cover" (the whole thing) design and arrangement.

Here are the parameters for the cover designs:

• eBook: 1600 x 2560 pixels, 72 ppi, RGB colorspace

• Physical book: 8.5 x 5.5 inches, 300 ppi, CMYK colorspace

For the physical book, if the designers don't extend the artwork to go outside the entire book, no bleeds need to be added.

We'll need the following from the winning designer(s):

1. An editable source file of the cover design, with open layers (AI; PSD); and

2. The fonts used. My brand fonts are Zing Rust Base, and Overpass. Those should be used, however I'm also open to alternative ideas as an additional consideration.

```html
<!DOCTYPE html>
<html lang="en">
<head>
<meta charset="utf-8">
<title>The Velvet Ledger Habit – Cover Options</title>
<link href="https://fonts.googleapis.com/css2?family=Bebas+Neue&display=swap" rel="stylesheet">
<style>
  :root {
    --page-bg: #ffffff;
    --label-grey: #7a7a7a;
    --cover-navy: #03287a;
    --jar-tone: #022270;
    --subtitle-blue: #1f57f2;
    --title-white: #ffffff;
  }
  * { margin: 0; padding: 0; box-sizing: border-box; }
  html, body {
    width: 1029px;
    height: 1200px;
    overflow: hidden;
    background: var(--page-bg);
  }
  .board {
    position: relative;
    width: 1029px;
    height: 1200px;
    font-family: "Bebas Neue", "Oswald", sans-serif;
  }
  .option {
    position: absolute;
    top: 0;
    width: 290px;
  }
  .option--one { left: 130px; }
  .option--two { left: 599px; }
  .option-label {
    position: absolute;
    top: 56px;
    width: 100%;
    text-align: center;
    font-size: 20px;
    letter-spacing: 0.5px;
    color: var(--label-grey);
  }
  .cover {
    position: absolute;
    top: 130px;
    width: 290px;
    height: 464px;
    background: var(--cover-navy);
    overflow: hidden;
  }
  .cover-subtitle {
    position: absolute;
    width: 100%;
    text-align: center;
    font-size: 17px;
    line-height: 22px;
    color: var(--subtitle-blue);
  }
  .cover-author {
    position: absolute;
    width: 100%;
    text-align: center;
    font-size: 26px;
    line-height: 28px;
    color: var(--title-white);
  }
  .option--one .cover-subtitle { top: 54px; }
  .option--one .cover-author { top: 356px; }
  .option--two .cover-author { top: 70px; }
  .option--two .cover-subtitle { top: 366px; }
  .jar-art {
    position: absolute;
    left: 83px;
    top: 136px;
    width: 110px;
    height: 116px;
  }
  .cover-title {
    position: absolute;
    top: 160px;
    width: 100%;
    text-align: center;
    color: var(--title-white);
    line-height: 0.9;
  }
  .cover-title span { display: block; }
  .title-small { font-size: 30px; }
  .title-large { font-size: 50px; }
</style>
</head>
<body>
<main class="board">

  <section class="option option--one">
    <h2 class="option-label">Cover 1</h2>
    <div class="cover">
      <p class="cover-subtitle">How to re-engage &amp;<br>reignite your workforce</p>
      <svg class="jar-art" viewBox="0 0 110 116" role="img" aria-label="Line drawing of a glass jar behind the title">
        <rect width="110" height="116" rx="40" fill="var(--jar-tone)"/>
      </svg>
      <h1 class="cover-title">
        <span class="title-small">The</span>
        <span class="title-large">Velvet Ledger</span>
        <span class="title-large">Habit</span>
      </h1>
      <p class="cover-author">Martin Calloway Jr</p>
    </div>
  </section>

  <section class="option option--two">
    <h2 class="option-label">Cover 2</h2>
    <div class="cover">
      <p class="cover-author">Martin Calloway Jr</p>
      <svg class="jar-art" viewBox="0 0 110 116" role="img" aria-label="Line drawing of a glass jar behind the title">
        <rect width="110" height="116" rx="40" fill="var(--jar-tone)"/>
      </svg>
      <h1 class="cover-title">
        <span class="title-small">The</span>
        <span class="title-large">Velvet Ledger</span>
        <span class="title-large">Habit</span>
      </h1>
      <p class="cover-subtitle">How to re-engage &amp;<br>reignite your workforce</p>
    </div>
  </section>

</main>
</body>
</html>
```